Varnock Travel letterhead design

We need a design for a simple document where we can dump our own information within it. A simple letterhead style. No address or phone details etc are required. More just our logo and free format. Hope this makes sense !

```html
<!DOCTYPE html>
<html lang="en">
<head>
<meta charset="utf-8">
<title>Varnock Travel Letterhead</title>
<link rel="stylesheet" href="https://fonts.googleapis.com/css2?family=Arimo:wght@400;700&display=swap">
<style>
  :root {
    --backdrop: #dcdcdc;
    --paper: #ffffff;
    --paper-tint: #fdfdfe;
    --brand-blue: #1f3f78;
    --rail-grey: #b9babd;
    --caption-grey: #8e9094;
  }
  * { margin: 0; padding: 0; box-sizing: border-box; }
  html, body {
    width: 1200px;
    height: 947px;
    overflow: hidden;
    background: var(--backdrop);
    font-family: "Arimo", Arial, sans-serif;
  }
  .letterhead {
    position: absolute;
    left: 364px;
    top: 179px;
    width: 472px;
    height: 605px;
    background: var(--paper);
  }
  .letterhead__pattern {
    position: absolute;
    left: 13px;
    top: 0;
    right: 0;
    bottom: 0;
    background: var(--paper-tint);
  }
  .letterhead__rail-accent {
    position: absolute;
    left: 0;
    top: 0;
    width: 13px;
    height: 80px;
    background: var(--brand-blue);
  }
  .letterhead__rail {
    position: absolute;
    left: 0;
    top: 83px;
    width: 13px;
    bottom: 0;
    background: var(--rail-grey);
  }
  .brand {
    position: absolute;
    left: 0;
    right: 0;
    top: 12px;
    text-align: center;
    padding-left: 0;
  }
  .brand__name {
    display: block;
    font-weight: 700;
    font-size: 22px;
    line-height: 22px;
    letter-spacing: -0.6px;
    color: var(--brand-blue);
  }
  .brand__tagline {
    display: block;
    margin-top: 1px;
    font-weight: 400;
    font-size: 7.6px;
    letter-spacing: 0.1px;
    color: var(--caption-grey);
  }
</style>
</head>
<body>
  <main class="letterhead">
    <div class="letterhead__pattern" role="img" aria-label="Faint diagonal repeated brand-name watermark pattern across the page"></div>
    <div class="letterhead__rail-accent"></div>
    <div class="letterhead__rail"></div>
    <header class="brand">
      <span class="brand__name">Varnock</span>
      <span class="brand__tagline">TRAVEL CORPORATION</span>
    </header>
  </main>
</body>
</html>
```